Attorney Business Card

I need a business card that looks professional yet modern. I am an Attorney. , I need a professional yet modern business card for my law practice. My logo and information have been uploaded. , I need a business card that looks professional yet modern. I am an Attorney. , I need a professional yet modern business card for my law practice. My logo and information have been uploaded.

Industry/Entity Type

Business

Requirements
Must have
• My logo which has been uploaded , my logo , My logo which has been uploaded , my logo

```html
<!DOCTYPE html>
<html lang="en">
<head>
<meta charset="utf-8">
<title>Marlowe Law Firm – Business Card</title>
<link href="https://fonts.googleapis.com/css2?family=Open+Sans:wght@400;600&display=swap" rel="stylesheet">
<style>
  :root {
    --bg-light: #e9e9e9;
    --bg-dark: #b9b9b9;
    --card-dark: #333435;
    --card-blue: #1b93cf;
    --brand-blue: #2a9fd8;
    --text-light: #e6e6e6;
    --text-muted: #b5b5b5;
    --divider: #6a6a6a;
  }
  * { box-sizing: border-box; margin: 0; padding: 0; }
  html, body { width: 1200px; height: 1000px; overflow: hidden; }
  body {
    font-family: "Open Sans", sans-serif;
    background: linear-gradient(160deg, var(--bg-light), var(--bg-dark));
    position: relative;
  }
  .card {
    position: absolute;
    width: 580px;
    height: 330px;
    background: var(--card-dark);
    box-shadow: 0 10px 30px rgba(0,0,0,0.35);
    overflow: hidden;
  }
  /* Front */
  .card-front { left: 560px; top: 70px; }
  .front-band { position: absolute; left: 0; bottom: 0; width: 580px; height: 150px; }
  .brand {
    display: flex; align-items: center; gap: 12px;
    color: var(--brand-blue); font-weight: 600; line-height: 1.25;
  }
  .brand-dot {
    width: 22px; height: 22px; border-radius: 50%;
    background: var(--brand-blue); flex: none;
  }
  .card-front .brand { position: absolute; left: 28px; top: 38px; width: 150px; font-size: 20px; }
  .front-title { position: absolute; right: 28px; top: 40px; text-align: right; color: var(--text-light); }
  .front-title .name { font-size: 30px; letter-spacing: 0.5px; white-space: nowrap; }
  .front-title .role { font-size: 21px; margin-top: 6px; letter-spacing: 0.5px; }
  .address {
    position: absolute; right: 34px; bottom: 28px;
    color: #ffffff; font-size: 17px; line-height: 1.75;
    display: grid; grid-template-columns: auto auto; column-gap: 6px;
  }
  .address .label { grid-row: 1; }
  .address span:not(.label) { grid-column: 2; }
  /* Back */
  .card-back { left: 60px; top: 520px; }
  .back-identity { position: absolute; left: 30px; top: 90px; width: 270px; text-align: center; }
  .card-back .brand { justify-content: center; font-size: 20px; }
  .back-name { color: var(--text-light); font-size: 34px; margin-top: 26px; white-space: nowrap; }
  .back-divider {
    position: absolute; left: 310px; top: 30px; bottom: 30px;
    border-left: 2px dotted var(--divider);
  }
  .contact-list { position: absolute; left: 334px; top: 42px; right: 20px; list-style: none; }
  .contact-item { display: flex; align-items: center; gap: 14px; height: 62px; color: var(--text-muted); font-size: 24px; white-space: nowrap; }
  .contact-item.email { font-size: 16px; }
  .contact-item svg { width: 30px; height: 30px; fill: var(--text-muted); flex: none; }
</style>
</head>
<body>

<section class="card card-front">
  <svg class="front-band" viewBox="0 0 580 150" aria-hidden="true">
    <path d="M0 20 H290 Q300 20 305 10 Q310 0 322 0 H570 Q580 0 580 10 V150 H0 Z" fill="var(--card-blue)"/>
  </svg>
  <div class="brand"><span class="brand-dot"></span><span>Marlowe Law Firm</span></div>
  <div class="front-title">
    <p class="name">Daniel Marlowe, ESQ</p>
    <p class="role">ATTORNEY AT LAW</p>
  </div>
  <p class="address">
    <span class="label">Address:</span>
    <span>1820 Cedar Ridge Ave.</span>
    <span>Suite 400</span>
    <span>Westbrook, CA 90510</span>
  </p>
</section>

<section class="card card-back">
  <div class="back-identity">
    <div class="brand"><span class="brand-dot"></span><span>Marlowe Law Firm</span></div>
    <p class="back-name">Daniel Marlowe</p>
  </div>
  <div class="back-divider"></div>
  <ul class="contact-list">
    <li class="contact-item mobile">
      <svg viewBox="0 0 24 24" aria-hidden="true"><path d="M8 2h8a1.5 1.5 0 0 1 1.5 1.5v17A1.5 1.5 0 0 1 16 22H8a1.5 1.5 0 0 1-1.5-1.5v-17A1.5 1.5 0 0 1 8 2zm0 2.5V11h8V4.5zM9 13v1.5h1.5V13zm2.3 0v1.5h1.5V13zm2.2 0v1.5H15V13zM9 16v1.5h1.5V16zm2.3 0v1.5h1.5V16zm2.2 0v1.5H15V16z"/></svg>
      555.318.2207
    </li>
    <li class="contact-item email">
      <svg viewBox="0 0 24 24" aria-hidden="true"><path d="M2 6l10 7 10-7v12H2zM3 5h18l-9 6.3z"/></svg>
      DANIEL@MLFIRM.COM
    </li>
    <li class="contact-item phone">
      <svg viewBox="0 0 24 24" aria-hidden="true"><path d="M3 8c0-2 3-3.5 9-3.5S21 6 21 8v1.5h-4.5V8h-9v1.5H3zM7 11h10l3 5v4H4v-4zm5 1.8a2.6 2.6 0 1 0 0 5.2 2.6 2.6 0 0 0 0-5.2z"/></svg>
      555.210.4400
    </li>
    <li class="contact-item fax">
      <svg viewBox="0 0 24 24" aria-hidden="true"><path d="M7 2h8l3 3v5H7zM3 11h18v10H3zm13 3v1.5h3V14zm0 3v1.5h3V17z"/></svg>
      555.210.4488
    </li>
  </ul>
</section>

</body>
</html>
```